Business Card for IT company

I need a high tech looking business card using our logo. I prefer something clean and modern.

Target Market(s)

Buyers of IT hardware and software, IT Techies who are key influencers

Industry/Entity Type

Business

```html
<!DOCTYPE html>
<html lang="en">
<head>
<meta charset="utf-8">
<title>KTRX Consulting – Business Card</title>
<link href="https://fonts.googleapis.com/css2?family=Montserrat:wght@400;600;700;800&display=swap" rel="stylesheet">
<style>
  :root {
    --stage: #6e6e6e;
    --green: #4aa83c;
    --black: #2a2a2a;
    --paper: #e8e9eb;
    --ink: #2c2c2c;
    --ink-soft: #444444;
    --slash: #f4f4f4;
  }
  * { margin: 0; padding: 0; box-sizing: border-box; }
  html, body {
    width: 1200px; height: 787px; overflow: hidden;
    background: var(--stage);
    font-family: "Montserrat", Arial, sans-serif;
  }
  .stage {
    position: relative; width: 1200px; height: 787px;
    display: flex; align-items: center; justify-content: center; gap: 60px;
  }
  .card {
    position: relative; width: 520px; height: 300px;
    box-shadow: 0 10px 24px rgba(0,0,0,0.35);
  }
  .card-frame { position: absolute; inset: 0; width: 100%; height: 100%; display: block; }
  .card-content { position: absolute; inset: 0; }

  /* Front */
  .front .brand {
    position: absolute; left: 0; right: 0; top: 86px;
    text-align: center; color: var(--ink);
  }
  .front .brand-name {
    font-weight: 800; font-size: 64px; line-height: 1; letter-spacing: 1px;
  }
  .front .brand-sub {
    margin-top: 8px; font-weight: 800; font-size: 22px; letter-spacing: 9px;
  }
  .front .website {
    margin-top: 8px; font-weight: 600; font-size: 14px; letter-spacing: 2px; color: var(--ink-soft);
  }

  /* Back */
  .back .brand {
    position: absolute; left: 50px; top: 106px; color: var(--ink);
  }
  .back .brand-name { font-weight: 800; font-size: 44px; line-height: 1; letter-spacing: 1px; }
  .back .brand-sub { margin-top: 4px; font-weight: 800; font-size: 15px; letter-spacing: 6px; }
  .back .person {
    position: absolute; right: 60px; top: 46px; text-align: left;
  }
  .back .person-name { font-weight: 800; font-size: 15px; color: var(--ink); letter-spacing: 0.5px; }
  .back .person-role { font-weight: 600; font-size: 8px; color: var(--ink-soft); margin-top: 2px; }
  .back .contact {
    position: absolute; right: 50px; top: 176px;
    list-style: none; font-size: 10px; font-weight: 400; color: var(--ink); line-height: 16px;
  }
  .back .contact span { font-weight: 600; margin-right: 4px; }
</style>
</head>
<body>
<main class="stage">

  <section class="card front" aria-label="Business card front">
    <svg class="card-frame" viewBox="0 0 520 300" aria-hidden="true">
      <rect width="520" height="300" fill="var(--green)"/>
      <polygon points="0,160 0,300 120,300" fill="var(--black)"/>
      <polygon points="410,0 520,0 520,95" fill="var(--black)"/>
      <line x1="0" y1="148" x2="128" y2="300" stroke="var(--slash)" stroke-width="4"/>
      <line x1="398" y1="0" x2="520" y2="106" stroke="var(--slash)" stroke-width="4"/>
      <rect x="22" y="22" width="476" height="256" fill="var(--paper)"/>
    </svg>
    <div class="card-content">
      <div class="brand">
        <div class="brand-name">KTRX</div>
        <div class="brand-sub">CONSULTING</div>
        <div class="website">www.yourwebsite.com</div>
      </div>
    </div>
  </section>

  <section class="card back" aria-label="Business card back">
    <svg class="card-frame" viewBox="0 0 520 300" aria-hidden="true">
      <rect width="520" height="300" fill="var(--black)"/>
      <polygon points="360,0 520,0 520,95" fill="var(--green)"/>
      <line x1="348" y1="0" x2="520" y2="106" stroke="var(--slash)" stroke-width="4"/>
      <rect x="22" y="22" width="476" height="256" fill="var(--paper)"/>
    </svg>
    <div class="card-content">
      <div class="person">
        <div class="person-name">JOHN DOE</div>
        <div class="person-role">Graphic Designer</div>
      </div>
      <div class="brand">
        <div class="brand-name">KTRX</div>
        <div class="brand-sub">CONSULTING</div>
      </div>
      <ul class="contact">
        <li><span>Tel:</span>(000) 1234 5678</li>
        <li><span>Fax:</span>(000) 1234 5679</li>
        <li><span>Email:</span>mail@yourdomain.com</li>
        <li><span>Web:</span>www.yourwebsite.com</li>
      </ul>
    </div>
  </section>

</main>
</body>
</html>
```